Super Creative! Copper Lantern Ad

CREATIVE CREATIVE CREATIVE needed for our Ad that will be placed on Google Ads, in print and on billboards. Our website is https://mycopperlantern.example

Target Market(s)

B2B

Requirements
Must have
• Uniqueness, creative and the following marks and copy:
1. our logo
2. Our phone number: (555) 274-8830
3. Our website address: mycopperlantern.example
4. Main message: BUILD BRAND. SUSTAIN GROWTH CURVE.

```html
<!DOCTYPE html>
<html lang="en">
<head>
<meta charset="UTF-8">
<title>Copper Lantern Banner</title>
<link href="https://fonts.googleapis.com/css2?family=Poppins:wght@300;600;700&display=swap" rel="stylesheet">
<style>
  :root {
    --backdrop: #d5d4d2;
    --charcoal: #363334;
    --white: #ffffff;
    --sky-top: #54c9f4;
    --sky-bottom: #2d8ecd;
  }
  * { margin: 0; padding: 0; box-sizing: border-box; }
  html, body {
    width: 1200px; height: 1200px; overflow: hidden;
    background: var(--backdrop);
    font-family: "Poppins", sans-serif;
  }
  .banner {
    position: absolute; left: 94px; top: 431px;
    width: 1011px; height: 337px;
    background: var(--charcoal);
    overflow: hidden;
  }
  .banner-shapes { position: absolute; inset: 0; }
  .brand {
    position: absolute; left: 453px; top: 47px; height: 53px;
    display: flex; align-items: center; gap: 14px;
  }
  .brand-dot {
    width: 44px; height: 44px; border-radius: 50%;
    background: linear-gradient(var(--sky-top), var(--sky-bottom));
  }
  .brand-name {
    color: var(--white); font-weight: 600; font-size: 36px;
    letter-spacing: 0.5px; line-height: 1;
  }
  .slogan {
    position: absolute; left: 354px; right: 0; top: 141px;
    text-align: center; color: var(--white);
    font-weight: 700; font-size: 34px; line-height: 36px;
    letter-spacing: 0.3px;
  }
  .contact {
    position: absolute; top: 274px; height: 38px;
    display: flex; align-items: center; gap: 10px;
    color: var(--white); font-weight: 300; font-size: 23px;
  }
  .contact-phone { left: 369px; }
  .contact-web { left: 661px; }
  .contact-divider {
    position: absolute; left: 612px; top: 274px;
    width: 3px; height: 38px; background: var(--sky-top);
  }
  .icon { width: 31px; height: 31px; flex: none; }
</style>
</head>
<body>
  <div class="banner">
    <svg class="banner-shapes" width="1011" height="337" viewBox="0 0 1011 337">
      <defs>
        <linearGradient id="sky" x1="0" y1="0" x2="0" y2="1">
          <stop offset="0" stop-color="#54c9f4"/>
          <stop offset="1" stop-color="#2d8ecd"/>
        </linearGradient>
      </defs>
      <path class="side-panel" d="M0 0 H235 C300 30 346 95 346 169 C346 243 300 307 235 337 H0 Z" fill="#ffffff"/>
      <path class="side-panel-fill" d="M0 0 H186 C270 0 335 75 335 169 C335 263 270 337 186 337 H0 Z" fill="url(#sky)"/>
      <path class="slogan-band" d="M354 135 H1011 V240 H342 C354 215 362 190 357 169 C358 155 356 145 354 135 Z" fill="url(#sky)"/>
    </svg>

    <div class="brand">
      <span class="brand-dot"></span>
      <span class="brand-name">COPPER LANTERN</span>
    </div>

    <p class="slogan">BUILD BRAND.<br>SUSTAIN GROWTH CURVE.</p>

    <div class="contact contact-phone">
      <svg class="icon" viewBox="0 0 32 32" aria-hidden="true">
        <circle cx="16" cy="16" r="16" fill="#54c9f4"/>
        <path d="M10 8 l3 -1 l2 5 l-2 1.5 c1 2.5 2.5 4 5 5 l1.5 -2 l5 2 l-1 3 c-8 0 -13.5 -5.5 -13.5 -13.5 z" fill="#363334"/>
      </svg>
      <span>(555) 274-8830</span>
    </div>

    <span class="contact-divider"></span>

    <div class="contact contact-web">
      <svg class="icon" viewBox="0 0 32 32" aria-hidden="true" fill="none" stroke="#54c9f4" stroke-width="1.6">
        <circle cx="16" cy="16" r="13"/>
        <ellipse cx="16" cy="16" rx="6" ry="13"/>
        <line x1="16" y1="3" x2="16" y2="29"/>
        <line x1="3" y1="16" x2="29" y2="16"/>
        <path d="M5 9 H27 M5 23 H27"/>
      </svg>
      <span>mycopperlantern.example</span>
    </div>
  </div>
</body>
</html>
```